Bright Harbor Workshops business card design

Needing a business card design using an existing logo. Double sided card and we will be printing using rounded corners. Can also use metallics if appropriate. The design needs to be professional and modern.

Target Market(s)

Professional organisations

Industry/Entity Type

Business

Contact Information for Business Card

busines name, person name, email, website, phone, address,

Colors

Designer to choose colors to be used in the design.

Requirements
Must have
• Use existing 'Bright Harbor Workshops' logo Using uploaded logo design. Simple and modern design. Black,white,silver,greys as the dominant colouring. Can introduce another single colour. Must also include a small version of the attached 'KDL' logo on the card (white and black versions uploaded also)
Nice to have
• Something modern
Should not have
• Additional images

```html
<!DOCTYPE html>
<html lang="en">
<head>
<meta charset="utf-8">
<title>Bright Harbor Workshops – Business Card</title>
<link rel="stylesheet" href="https://fonts.googleapis.com/css2?family=Marcellus&family=Noto+Serif:wght@400;700&family=Open+Sans:wght@400;600&display=swap">
<style>
  :root {
    --page-bg: #efede9;
    --card-frost: #d8d4cf;
    --panel-grey: #e5e5e5;
    --silver: #b9b2a8;
    --ink: #111111;
    --ink-soft: #2a2a2a;
    --rule: #555555;
  }
  * { margin: 0; padding: 0; box-sizing: border-box; }
  html, body {
    width: 1200px; height: 902px; overflow: hidden;
    background: var(--page-bg);
  }
  .card {
    position: absolute; left: 100px; top: 166px;
    width: 1000px; height: 570px;
    border-radius: 28px; overflow: hidden;
    background: linear-gradient(135deg, #dcd9d5 0%, var(--card-frost) 55%, #d2cdc8 100%);
    box-shadow: 0 6px 24px rgba(0,0,0,0.12);
  }
  .card-shape { position: absolute; inset: 0; }
  .brand {
    position: absolute; left: 74px; top: 190px;
    display: flex; align-items: flex-start; gap: 18px;
  }
  .brand-dot {
    width: 58px; height: 58px; border-radius: 50%;
    border: 5px solid var(--ink); margin-top: 6px;
  }
  .brand-name {
    font-family: "Marcellus", serif;
    font-size: 38px; line-height: 1.08; letter-spacing: 2px;
    color: var(--ink); text-align: right;
  }
  .brand-tagline {
    position: absolute; left: 72px; top: 352px; width: 290px;
    text-align: right;
    font-family: "Noto Serif", serif; font-weight: 700;
    font-size: 13px; color: var(--ink);
  }
  .contact {
    position: absolute; left: 596px; top: 142px;
    font-family: "Noto Serif", serif; color: var(--ink);
  }
  .contact-name { font-size: 31px; font-weight: 700; letter-spacing: 0.5px; line-height: 1.1; }
  .contact-role { font-size: 22px; line-height: 1.4; }
  .contact-address { margin-top: 30px; font-size: 22px; line-height: 1.5; }
  .contact-lines { margin-top: 24px; list-style: none; font-size: 22px; line-height: 1.7; }
  .contact-lines li { display: flex; align-items: center; gap: 8px; }
  .contact-icon { width: 28px; height: 28px; flex: none; }
  .membership {
    position: absolute; left: 778px; top: 466px;
    display: flex; align-items: center; gap: 10px;
    font-family: "Open Sans", sans-serif; color: var(--ink-soft);
  }
  .membership-mark { display: flex; flex-direction: column; align-items: center; gap: 2px; }
  .membership-dot { width: 30px; height: 30px; border-radius: 50%; background: var(--ink); }
  .membership-name { font-size: 22px; font-weight: 400; line-height: 1; }
  .membership-rule { width: 1px; height: 58px; background: var(--rule); }
  .membership-text { font-size: 11px; line-height: 1.3; }
</style>
</head>
<body>
  <div class="card">
    <svg class="card-shape" viewBox="0 0 1000 570" width="1000" height="570" aria-hidden="true">
      <defs>
        <linearGradient id="silverEdge" x1="0" y1="0" x2="0" y2="1">
          <stop offset="0" stop-color="#c9c3ba"/>
          <stop offset="0.5" stop-color="#9e958a"/>
          <stop offset="1" stop-color="#cfc9c0"/>
        </linearGradient>
      </defs>
      <path d="M655 0 C575 60 555 190 590 290 C615 370 700 450 690 570 L1000 570 L1000 0 Z" fill="var(--panel-grey)"/>
      <path d="M640 40 C585 110 575 210 605 295 C630 370 705 440 700 560" fill="none" stroke="url(#silverEdge)" stroke-width="4" stroke-linecap="round"/>
    </svg>

    <div class="brand">
      <span class="brand-dot"></span>
      <div class="brand-name">BRIGHT<br>HARBOR<br>WORKSHOPS</div>
    </div>
    <p class="brand-tagline">Evidence-Based Training &amp; Development</p>

    <div class="contact">
      <p class="contact-name">JONAH WELLS</p>
      <p class="contact-role">Managing Partner</p>
      <p class="contact-address">PO BOX 418 Harbor Lane<br>12 Quay Street, Portfield</p>
      <ul class="contact-lines">
        <li>
          <svg class="contact-icon" viewBox="0 0 28 28" aria-hidden="true">
            <rect width="28" height="28" rx="4" fill="#111"/>
            <path d="M7 11 Q14 5 21 11 L19 13 L17 11 L11 11 L9 13 Z" fill="#fff"/>
            <rect x="8" y="14" width="12" height="8" rx="1.5" fill="#fff"/>
          </svg>
          <span>(02) 4816 3370</span>
        </li>
        <li>
          <svg class="contact-icon" viewBox="0 0 28 28" aria-hidden="true">
            <rect width="28" height="28" rx="4" fill="#111"/>
            <rect x="5" y="8" width="18" height="12" fill="none" stroke="#fff" stroke-width="1.8"/>
            <path d="M5 8 L14 15 L23 8" fill="none" stroke="#fff" stroke-width="1.8"/>
          </svg>
          <span>hello@brightharbor.co</span>
        </li>
      </ul>
    </div>

    <div class="membership">
      <div class="membership-mark">
        <span class="membership-dot"></span>
        <span class="membership-name">KDL</span>
      </div>
      <span class="membership-rule"></span>
      <p class="membership-text">Member<br>Kestrel<br>Development<br>League MKDL</p>
    </div>
  </div>
</body>
</html>
```